Stylist/Barber Standup Sign for Hair Regrowth Company

We want to design an attractive and eye-catching sign for hair stylists and barbers to sit on their workstations to attract the attention of their clients regarding hair loss and encourage them to speak to their stylist about it of they are would like to seek treatment.
50% of men and 25% of women suffer from hair loss but most are in denial that it is happening or too embarrassed to talk about it.

Copy for the flyer is as follows:

[Section 1:]
This flyer has been placed here/designed to spark conversation about hair loss

[Section 2:]
The truth is...
73% of people believe their hair is thinning
They are right

[Section 3:]
If you've got questions, your stylist or barber has answers.

Additional Background Information:

Primary target audience is men between the ages of 25-45, secondary target audience is men 46-60

Current Consumer Perception? (in the first person) “I’ve been thinking about my hair. I think it’s getting thinner and I’m scared, worried and don’t know what to do. But I don’t know if there is anything that really works. I’ve tried other things and nothing‘s worked.”

Tonality of materials? Very guy friendly, matter of fact, authoritative, its what you might hear from your best friend. Confident. Encouraging, but with a sense of urgency.

Please use our brand colors, but do not include our logo or brand name.
Colors are as follows:
Green: #4ca26f
Light Grey: #999999
Dark Grey: #262626

I have attached print templates in both PDF and Jpeg, please use those to provide final ready to print documents if you are selected.

Target Market(s)

Industry/Entity Type

Health And Wellness

Font styles to use
Sans Serif

Colors
00a990
ffffff
333333
cbcbcb

Requirements
Must have
• We want to get across the following messaging. Ideally you will submit a design using our copy and if you think you can do better, please feel free to submit another design with your own copy/messaging. If you can do it better we would love to select you :-)
• Our copy?
• This flyer has been placed here/designed to spark conversation about hair loss
• The truth is...
• 73% of people believe their hair is thinning
• They are right
• If you've got questions, your stylist or barber has answers
• Also please use our brand colors:
• Green: #4ca26f
• Light Grey: #999999
• Dark Grey: #262626
Should not have
• dont add any logos, images or ornate design. this needs to be simple, easy to ready and eye catching.
• do not use the color red in any capacity.

```html
<!DOCTYPE html>
<html lang="en">
<head>
<meta charset="utf-8">
<title>Hair Loss Conversation Sign</title>
<link rel="stylesheet" href="https://fonts.googleapis.com/css2?family=Chewy&family=Roboto:wght@300;400;700;900&display=swap">
<style>
  :root {
    --green: #44e27c;
    --white: #ffffff;
    --ink: #231f20;
    --band-grey: #c9cdd0;
    --shadow: rgba(20, 70, 40, 0.55);
  }
  * { margin: 0; padding: 0; box-sizing: border-box; }
  html, body { width: 809px; height: 1200px; overflow: hidden; background: var(--white); }
  .sign {
    position: relative;
    width: 809px;
    height: 1200px;
    overflow: hidden;
    background: var(--white);
    font-family: "Roboto", Arial, sans-serif;
  }
  .sign__crown { position: absolute; left: 0; top: 0; width: 809px; height: 400px; }
  .sign__body { position: absolute; left: 0; top: 385px; width: 809px; height: 815px; background: var(--green); }
  .hook-line {
    font-family: "Chewy", "Arial Rounded MT Bold", "Arial Black", sans-serif;
    font-weight: 700;
    fill: var(--white);
    filter: drop-shadow(4px 8px 5px var(--shadow));
  }
  .moustache-art {
    position: absolute;
    left: 45px; top: 395px;
    width: 720px; height: 195px;
    background: var(--white);
    border-radius: 60px 60px 120px 120px;
    box-shadow: 0 10px 12px var(--shadow);
  }
  .truth-lead {
    position: absolute;
    left: 68px; top: 622px;
    color: var(--white);
    font-weight: 700;
    font-size: 62px;
    letter-spacing: 0.5px;
    line-height: 1.1;
  }
  .stat-band {
    position: absolute;
    left: 0; top: 712px;
    width: 809px; height: 106px;
    background: var(--band-grey);
    color: var(--ink);
  }
  .stat-band__figure {
    position: absolute;
    left: 40px; top: -6px;
    font-size: 118px;
    line-height: 118px;
    font-weight: 700;
    letter-spacing: -2px;
  }
  .stat-band__text {
    position: absolute;
    left: 305px; top: 20px;
    font-size: 29px;
    line-height: 36px;
    font-weight: 400;
  }
  .stat-band__text strong { font-weight: 700; }
  .stat-band__text .big { font-size: 38px; font-weight: 700; }
  .verdict-band {
    position: absolute;
    left: 0; top: 818px;
    width: 809px; height: 52px;
    background: var(--ink);
    color: var(--white);
    display: flex;
    align-items: center;
    justify-content: flex-end;
    padding-right: 64px;
    gap: 16px;
    font-size: 28px;
    font-weight: 700;
  }
  .verdict-band span { font-weight: 400; }
  .verdict-band strong { font-weight: 700; }
  .question-backdrop { position: absolute; left: 0; top: 870px; width: 809px; height: 330px; }
  .answer-copy { position: absolute; left: 0; top: 0; width: 809px; color: var(--white); }
  .answer-copy p { position: absolute; white-space: nowrap; line-height: 1; }
  .answer-copy .light { font-weight: 300; }
  .answer-copy .bold { font-weight: 700; }
  .answer-copy .small { font-weight: 400; }
  .line-one { left: 78px; top: 892px; }
  .line-two { left: 60px; top: 995px; }
  .line-three { left: 275px; top: 1078px; }
</style>
</head>
<body>
<main class="sign">
  <svg class="sign__crown" viewBox="0 0 809 400" aria-hidden="true">
    <path fill="var(--green)" d="M0 330 C 10 260, 35 210, 55 150 C 80 80, 130 40, 210 30 C 310 15, 430 -5, 560 25 C 640 45, 690 70, 710 130 C 730 180, 750 230, 809 250 L 809 400 L 0 400 Z"/>
  </svg>
  <div class="sign__body"></div>

  <svg class="sign__crown" viewBox="0 0 809 400" style="overflow:visible">
    <defs>
      <path id="hook-path-1" d="M125 130 C 320 100, 580 180, 730 390"/>
      <path id="hook-path-2" d="M92 222 C 270 175, 570 235, 712 445"/>
      <path id="hook-path-3" d="M65 310 C 210 268, 390 292, 500 348"/>
    </defs>
    <text class="hook-line" font-size="44"><textPath href="#hook-path-1">THiS FLyer HAS beeN PLACed</textPath></text>
    <text class="hook-line" font-size="42"><textPath href="#hook-path-2">Here to SpaRK conVerSation</textPath></text>
    <text class="hook-line" font-size="46"><textPath href="#hook-path-3">about Hair LOSS</textPath></text>
  </svg>

  <div class="moustache-art" role="img" aria-label="White moustache illustration"></div>

  <h1 class="truth-lead">The truth is...</h1>

  <section class="stat-band">
    <div class="stat-band__figure">73%</div>
    <p class="stat-band__text">of <strong>people believe</strong><br>their <strong class="big">hair</strong> is <strong class="big">thinning</strong></p>
  </section>

  <div class="verdict-band">
    <svg width="24" height="22" viewBox="0 0 24 22" aria-hidden="true"><path d="M2 12 L9 19 L22 3" fill="none" stroke="var(--white)" stroke-width="4.5"/></svg>
    <p><span>They are</span> <strong>right</strong></p>
  </div>

  <div class="question-backdrop" role="img" aria-label="Pattern of outlined question marks"></div>

  <div class="answer-copy">
    <p class="line-one"><span class="light" style="font-size:92px">If</span><span class="small" style="font-size:42px"> YOU’VE got </span><span class="bold" style="font-size:78px">questions</span><span class="small" style="font-size:40px">,</span></p>
    <p class="line-two"><span class="small" style="font-size:30px">your </span><span class="bold" style="font-size:74px">stylist</span><span class="small" style="font-size:28px"> or </span><span class="light" style="font-size:74px">barber</span></p>
    <p class="line-three"><span class="small" style="font-size:28px">has </span><span class="bold" style="font-size:92px">answers</span><span class="small" style="font-size:28px">.</span></p>
  </div>
</main>
</body>
</html>
```